Save the Date for 77th birthday fundraiser

We need a design for a Save the Date as we are preparing to celebrate our founder Dale Penwarden’s 77 birthday next year.
We would like a professional illustrated Save the Date with the theme “How it started, How it’s going”. Attached is a picture from the early 70’s and another one from yesterday. We want him to look his absolute best.
We need the date, location, and contact details to RSVP incorporated into the design:
April 9
Milford Avery House, Austin Texas
team@guidebrightpath.com
AND PLEASE REMEMBER THIS IS A SURPRISE!
We would also like to include elements that evoke what he does: Author (he’s published 2 books), Speaker (a microphone), Business Coach, and Entrepreneur.
Feelings we would like to evoke when people see the image: Would like people to think we are a professional company that is throwing a fun event for all the clients and friends Dale has made along his extraordinary 50-year career.
Thank you so much!

```html
<!DOCTYPE html>
<html lang="en">
<head>
<meta charset="utf-8">
<title>Save the Date – Dale Penwarden</title>
<link rel="stylesheet" href="https://fonts.googleapis.com/css2?family=Playball&family=Poppins:wght@400;500;700;800;900&display=swap">
<style>
  :root {
    --navy: #2b2d6b;
    --ink: #1c1f4f;
    --sky: #4da7de;
    --sky-pale: #b9dcef;
    --mint: #a9dbd8;
    --cream: #eef0e2;
    --white: #ffffff;
    --photo-old: #8a8a86;
    --photo-new: #9b4450;
    --mic: #34377a;
    --ribbon-fold: #4a2a1a;
  }
  * { box-sizing: border-box; margin: 0; padding: 0; }
  html, body { width: 950px; height: 1200px; overflow: hidden; }
  body { font-family: "Poppins", sans-serif; background: var(--cream); }

  .poster {
    position: relative;
    width: 950px;
    height: 1200px;
    overflow: hidden;
    background:
      repeating-conic-gradient(from 0deg at 50% 56%,
        rgba(185,220,239,.75) 0deg 5deg,
        rgba(238,240,226,0) 5deg 11deg,
        rgba(169,219,216,.55) 11deg 15deg,
        rgba(238,240,226,0) 15deg 22deg),
      var(--cream);
  }

  .brand { position: absolute; top: 14px; left: 0; width: 100%; text-align: center; color: var(--ink); z-index: 5; }
  .brand-name { font-family: "Playball", cursive; font-size: 74px; font-weight: 400; line-height: 1; }
  .brand-tagline { font-size: 18px; font-weight: 500; letter-spacing: 9.5px; margin-top: 12px; margin-left: 9px; line-height: 1; }

  .portrait-circle { position: absolute; border-radius: 50%; }
  .circle-then { left: 55px; top: 190px; width: 412px; height: 362px; border-radius: 50%; background: var(--navy); }
  .circle-now { left: 473px; top: 192px; width: 415px; height: 362px; border-radius: 50%; background: var(--sky); }

  .photo { position: absolute; }
  .photo-then { left: 62px; top: 138px; width: 382px; height: 428px;
    background: linear-gradient(180deg, #6d6d6a, var(--photo-old)); border: 4px solid var(--white); }
  .photo-now { left: 586px; top: 138px; width: 259px; height: 428px;
    background: linear-gradient(180deg, #3d3a3a 0 24%, #e9e4de 24% 42%, var(--photo-new) 42%); }

  .microphone { position: absolute; left: 440px; top: 330px; width: 92px; height: 300px; z-index: 3;
    background: linear-gradient(180deg, var(--mic) 0 58%, #4b4e92 58%); border-radius: 46px 46px 6px 6px; }

  .era-label { position: absolute; top: 566px; height: 62px; display: flex; align-items: center; justify-content: center;
    color: var(--white); font-weight: 800; font-size: 40px; letter-spacing: .5px; z-index: 2; }
  .label-then { left: 2px; width: 468px; background: var(--navy); border: 2px solid var(--white); outline: 2px solid var(--navy); }
  .label-now { left: 506px; width: 440px; background: var(--sky); border: 2px solid var(--white); outline: 2px solid var(--sky); }
  .underline { position: absolute; top: 636px; height: 11px; }
  .underline-then { left: 10px; width: 480px; background: var(--sky); }
  .underline-now { left: 497px; width: 453px; background: var(--navy); }

  .save-the-date { position: absolute; top: 672px; width: 100%; text-align: center; color: var(--ink); font-size: 31px; font-weight: 400; line-height: 1.2; }
  .event-date { position: absolute; top: 700px; width: 100%; text-align: center;
    font-size: 118px; font-weight: 800; line-height: 1.05; color: var(--navy);
    -webkit-text-stroke: 3px var(--white);
    text-shadow: 10px 8px 0 var(--sky); letter-spacing: 2px; }

  .venue-ribbon { position: absolute; left: 0; top: 838px; width: 950px; height: 125px; }
  .venue-text { position: absolute; top: 848px; width: 100%; text-align: center; color: var(--white); line-height: 1.15; }
  .venue-name { font-size: 31px; font-weight: 400; }
  .venue-city { font-size: 41px; font-weight: 500; line-height: 1.05; }

  .reminder { position: absolute; top: 982px; width: 100%; text-align: center; color: var(--navy); line-height: 1.05; }
  .reminder-lead { font-size: 62px; font-weight: 700; letter-spacing: 2px; text-shadow: 3px 3px 0 var(--sky); }
  .reminder-strong { font-size: 78px; font-weight: 900; letter-spacing: 1px; text-shadow: 4px 4px 0 var(--sky); }

  .contact-bar { position: absolute; left: 0; bottom: 0; width: 100%; height: 53px; background: var(--navy);
    display: flex; align-items: center; justify-content: center; gap: 16px; color: var(--white); font-size: 30px; }
</style>
</head>
<body>
<main class="poster">
  <header class="brand">
    <h1 class="brand-name">Dale Penwarden</h1>
    <p class="brand-tagline">GUIDE TO BRIGHT PATH</p>
  </header>

  <div class="portrait-circle circle-then"></div>
  <div class="portrait-circle circle-now"></div>

  <div class="photo photo-then" role="img" aria-label="Black and white 1970s photo of Dale in a top hat and tweed vest, hands on hips"></div>
  <div class="photo photo-now" role="img" aria-label="Recent photo of Dale in a top hat, white shirt and burgundy vest, hands on hips"></div>
  <div class="microphone" role="img" aria-label="Vintage navy microphone illustration"></div>

  <div class="era-label label-then">HOW IT STARTED</div>
  <div class="era-label label-now">HOW IT’S GOING</div>
  <div class="underline underline-then"></div>
  <div class="underline underline-now"></div>

  <p class="save-the-date">Save The Date</p>
  <p class="event-date">APRIL 9</p>

  <svg class="venue-ribbon" viewBox="0 0 950 125" aria-hidden="true">
    <polygon points="194,18 240,18 240,122 163,122 198,68" fill="var(--sky)"/>
    <polygon points="756,18 710,18 710,122 787,122 752,68" fill="var(--sky)"/>
    <line x1="198" y1="28" x2="224" y2="28" stroke="#fff" stroke-width="1.5" stroke-dasharray="6 4"/>
    <line x1="176" y1="112" x2="240" y2="112" stroke="#fff" stroke-width="1.5" stroke-dasharray="6 4"/>
    <line x1="726" y1="28" x2="752" y2="28" stroke="#fff" stroke-width="1.5" stroke-dasharray="6 4"/>
    <line x1="710" y1="112" x2="774" y2="112" stroke="#fff" stroke-width="1.5" stroke-dasharray="6 4"/>
    <polygon points="224,103 268,103 268,120" fill="var(--ribbon-fold)"/>
    <polygon points="726,103 682,103 682,120" fill="var(--ribbon-fold)"/>
    <rect x="224" y="0" width="502" height="104" fill="var(--navy)"/>
    <line x1="230" y1="6" x2="720" y2="6" stroke="#fff" stroke-width="1.5" stroke-dasharray="6 4"/>
    <line x1="230" y1="98" x2="720" y2="98" stroke="#fff" stroke-width="1.5" stroke-dasharray="6 4"/>
  </svg>
  <div class="venue-text">
    <p class="venue-name">Milford Avery House</p>
    <p class="venue-city">Austin Texas</p>
  </div>

  <div class="reminder">
    <p class="reminder-lead">AND PLEASE REMEMBER</p>
    <p class="reminder-strong">THIS IS A SURPRISE!</p>
  </div>

  <footer class="contact-bar">
    <svg width="40" height="28" viewBox="0 0 40 28" aria-hidden="true">
      <rect x="0" y="0" width="40" height="28" rx="2" fill="var(--white)"/>
      <polyline points="2,3 20,16 38,3" fill="none" stroke="var(--navy)" stroke-width="3"/>
    </svg>
    <span class="contact-email">team@guidebrightpath.com</span>
  </footer>
</main>
</body>
</html>
```